Project Manager Business Card for Top Architectural Firm

Update and design a stunning Senior Project Manager Business Card

MARCO T. RUEDA II
Senior Project Manager

H A R B O R L I N E
A R C H I T E C T U R E L L C.
www.HarborlineCrestHouses.com
4217 NW 38th Ter. Suite 905
Miami, FL 33172
C: (305) 418-2273
mrueda.harborlinecresthouses@mailvista.net

Looking to have the logo to be UV Spot ink printed and to be prominent.

Target Market(s)

High end real estate architecture construction

Industry/Entity Type

Architect

Contact Information for Business Card

MARCO T. RUEDA II
Senior Project Manager

H A R B O R L I N E
Miami, FL 33172
C: (305) 418-2273

Font styles to use
Sans Serif

Colors

Designer to choose colors to be used in the design.

Requirements
Must have
• Prominent Logo

```html
<!DOCTYPE html>
<html lang="en">
<head>
<meta charset="utf-8">
<title>Harborline Architecture – Business Card</title>
<link rel="stylesheet" href="https://fonts.googleapis.com/css2?family=Lato:wght@300;400;700;900&display=swap">
<style>
  :root {
    --backdrop: #cfd3d4;
    --paper: #f1f1ef;
    --ink: #161616;
    --accent: #2a8fd0;
    --edge: #3a97cf;
    --charcoal: #2b2b2b;
    --logo-grey: #bcbcbc;
  }
  * { box-sizing: border-box; margin: 0; padding: 0; }
  html, body {
    width: 1200px; height: 1050px; overflow: hidden;
    background: var(--backdrop);
    font-family: "Lato", sans-serif;
  }
  .sheet {
    position: relative; width: 1200px; height: 1050px;
    display: flex; flex-direction: column; align-items: center;
    justify-content: center; gap: 50px;
  }
  .card {
    position: relative; width: 770px; height: 440px;
    border-bottom: 6px solid var(--edge);
    box-shadow: 0 18px 40px rgba(0,0,0,0.18);
  }
  .card-front { background: var(--paper); color: var(--ink); }
  .card-back {
    background: var(--charcoal);
    display: flex; flex-direction: column; align-items: center; justify-content: center;
  }

  .brand { position: absolute; left: 60px; top: 48px; font-weight: 300; color: var(--ink); }
  .brand-name { font-size: 44px; letter-spacing: 9px; line-height: 1; }
  .brand-sub { font-size: 12px; letter-spacing: 5.5px; margin-top: 8px; }

  .person { position: absolute; left: 60px; top: 160px; }
  .person-name { font-weight: 900; font-size: 29px; letter-spacing: 1px; }
  .person-title { color: var(--accent); font-size: 19px; margin-top: 4px; }

  .address { position: absolute; left: 60px; top: 248px; font-size: 17px; line-height: 1.4; }

  .contacts { position: absolute; left: 60px; top: 310px; list-style: none; font-size: 17px; line-height: 1.5; }
  .contacts li { display: flex; align-items: center; gap: 10px; }
  .contacts svg { width: 15px; height: 15px; flex: none; }

  .back-dot { width: 70px; height: 70px; border-radius: 50%; background: var(--accent); margin-bottom: 26px; }
  .back-name { color: var(--logo-grey); font-weight: 300; font-size: 58px; letter-spacing: 12px; line-height: 1; }
  .back-sub { color: var(--logo-grey); font-weight: 300; font-size: 15px; letter-spacing: 7px; margin-top: 12px; }
</style>
</head>
<body>
<main class="sheet">
  <section class="card card-front">
    <div class="brand">
      <div class="brand-name">HARBORLINE</div>
      <div class="brand-sub">ARCHITECTURE LLC</div>
    </div>
    <div class="person">
      <div class="person-name">MARCO T. RUEDA II</div>
      <div class="person-title">Senior Project Manager</div>
    </div>
    <div class="address">
      <div>4217 NW 38th Ter. Suite 905</div>
      <div>Miami, FL 33172</div>
    </div>
    <ul class="contacts">
      <li>
        <svg viewBox="0 0 16 16" aria-hidden="true"><path fill="var(--accent)" d="M4 1l2.5 3-1.5 1.6c.8 1.8 2.2 3.3 4 4.2L10.6 8l3.4 2.3-1.3 3.2C7 13 2.6 8.6 2 3z"/></svg>
        <span>(305) 418-2273</span>
      </li>
      <li>
        <svg viewBox="0 0 16 16" aria-hidden="true"><rect x="1.5" y="3.5" width="13" height="9" fill="none" stroke="var(--accent)" stroke-width="1.3"/><path d="M1.5 3.5l6.5 5 6.5-5" fill="none" stroke="var(--accent)" stroke-width="1.3"/></svg>
        <span>mrueda.harborlinecresthouses@mailvista.net</span>
      </li>
      <li>
        <svg viewBox="0 0 16 16" aria-hidden="true"><g fill="none" stroke="var(--accent)" stroke-width="1.2"><circle cx="8" cy="8" r="6.3"/><ellipse cx="8" cy="8" rx="2.8" ry="6.3"/><path d="M1.7 8h12.6M2.8 4.8h10.4M2.8 11.2h10.4"/></g></svg>
        <span>www.HarborlineCrestHouses.com</span>
      </li>
    </ul>
  </section>

  <section class="card card-back">
    <div class="back-dot"></div>
    <div class="back-name">HARBORLINE</div>
    <div class="back-sub">ARCHITECTURE LLC</div>
  </section>
</main>
</body>
</html>
```